Need a business card design. I am a Self Empowerment Life Coach.

A Life Coach is - a professional relationship designed to enhance an individual's ability to focus, make effective changes, develop oneself, achieve desired goals and maximize success in life. Coaching is about getting the very best out of someone and enabling them to make decisions that will improve their life. It is a unique way to help people look at where they are now and where they would like to be, and helps bridge the gap.

Bright Path Coaching is motivational, inspiring, positive, exciting and action driven. By raising awareness and encouraging others to take responsibility for their life, coaching can help people rise to their challenge and go further than you ever thought possible.

Industry/Entity Type

Business

Other font styles liked:
• Bookman Old Style

Requirements
Must have
• Marla Thorncastle, QTV-AR
• Self Empowerment Coach
• 318.557.6021
• mt@thebloomingpathcoach.example
• The attached logo
Nice to have
• I would like to see some designs portrait and some landscape

```html
<!DOCTYPE html>
<html lang="en">
<head>
<meta charset="utf-8">
<title>Bright Path Coaching – Business Card</title>
<link href="https://fonts.googleapis.com/css2?family=Open+Sans:wght@400;600;700&display=swap" rel="stylesheet">
<style>
  :root {
    --backdrop: #e9e4dc;
    --card: #ffffff;
    --ink: #1f1f1f;
    --ink-soft: #3a3a3a;
    --swoosh-grey: #8a8a8a;
    --swoosh-black: #161818;
    --brand-grey: #5f6b6b;
    --icon: #6d6d6d;
  }
  * { box-sizing: border-box; margin: 0; padding: 0; }
  html, body {
    width: 1200px; height: 899px; overflow: hidden;
    background: var(--backdrop);
    font-family: "Open Sans", Arial, sans-serif;
  }
  .card {
    position: absolute; left: 100px; top: 164px;
    width: 1000px; height: 571px;
    background: var(--card);
    box-shadow: 0 6px 18px rgba(0,0,0,.18);
    overflow: hidden;
  }
  .card__swoosh { position: absolute; inset: 0; width: 100%; height: 100%; }
  .contact {
    position: absolute; left: 42px; top: 198px;
    list-style: none; color: var(--ink-soft);
    font-size: 19px; line-height: 27px;
  }
  .contact li { display: flex; align-items: flex-start; gap: 9px; }
  .contact svg { flex: none; margin-top: 4px; }
  .contact .indent { padding-left: 29px; }
  .brand {
    position: absolute; left: 340px; top: 228px;
    display: flex; align-items: center; gap: 12px;
  }
  .brand__dot {
    width: 26px; height: 26px; border-radius: 50%;
    background: var(--brand-grey);
  }
  .brand__name {
    font-weight: 700; font-size: 34px; color: var(--brand-grey);
    letter-spacing: .5px; white-space: nowrap;
  }
  .person {
    position: absolute; right: 150px; bottom: 46px; text-align: right;
    color: var(--ink); white-space: nowrap;
  }
  .person__name { font-weight: 700; font-size: 38px; line-height: 1.15; }
  .person__role { font-weight: 400; font-size: 32px; line-height: 1.2; }
</style>
</head>
<body>
  <section class="card">
    <svg class="card__swoosh" viewBox="0 0 1000 571" preserveAspectRatio="none" aria-hidden="true">
      <path fill="var(--swoosh-grey)" d="M560,0 C800,80 930,300 905,571 L1000,571 L1000,0 Z"/>
      <path fill="var(--swoosh-black)" d="M625,0 C845,90 965,300 940,571 L1000,571 L1000,0 Z"/>
      <path fill="var(--swoosh-grey)" d="M700,0 C880,120 965,330 952,571 L964,571 C980,330 900,120 716,0 Z"/>
    </svg>

    <ul class="contact">
      <li>
        <svg width="20" height="20" viewBox="0 0 20 20"><circle cx="10" cy="10" r="10" fill="var(--icon)"/><path d="M5 10.5 10 6l5 4.5M7 10v4h6v-4" fill="none" stroke="#fff" stroke-width="1.6"/></svg>
        <span>Suite # 410, Elm Court,</span>
      </li>
      <li class="indent">NY 10234</li>
      <li>
        <svg width="20" height="20" viewBox="0 0 20 20"><circle cx="10" cy="10" r="10" fill="var(--icon)"/><path d="M7 5c-1 1-1 3 1 6s4 4 5 3l1-1-2-2-1 1c-1-.5-2-1.5-2.5-2.5l1-1-2-2z" fill="#fff"/></svg>
        <span>318.557.6021</span>
      </li>
      <li>
        <svg width="20" height="20" viewBox="0 0 20 20"><circle cx="10" cy="10" r="10" fill="var(--icon)"/><rect x="7" y="4.5" width="6" height="11" rx="1" fill="#fff"/></svg>
        <span>318.557.6022</span>
      </li>
      <li>
        <svg width="20" height="20" viewBox="0 0 20 20"><circle cx="10" cy="10" r="10" fill="var(--icon)"/><rect x="5.5" y="7" width="9" height="7" fill="#fff"/><rect x="7" y="4.5" width="6" height="3" fill="#fff"/></svg>
        <span>318.557.6023</span>
      </li>
      <li>
        <svg width="20" height="20" viewBox="0 0 20 20"><circle cx="10" cy="10" r="10" fill="var(--icon)"/><rect x="5" y="6.5" width="10" height="7" fill="#fff"/><path d="M5 6.5l5 4 5-4" fill="none" stroke="var(--icon)" stroke-width="1.2"/></svg>
        <span>mt@thebloomingpathcoach.example</span>
      </li>
      <li>
        <svg width="20" height="20" viewBox="0 0 20 20"><circle cx="10" cy="10" r="10" fill="var(--icon)"/><circle cx="10" cy="10" r="5" fill="none" stroke="#fff" stroke-width="1.4"/><path d="M5 10h10M10 5v10" stroke="#fff" stroke-width="1.2"/></svg>
        <span>www.thebloomingpathcoach.example</span>
      </li>
    </ul>

    <div class="brand">
      <span class="brand__dot"></span>
      <span class="brand__name">Bright Path Coaching</span>
    </div>

    <div class="person">
      <p class="person__name">Marla Thorncastle, QTV-AR</p>
      <p class="person__role">Self Empowerment Coach</p>
    </div>
  </section>
</body>
</html>
```